Web Site

Target Market(s)

CEOs and International Sales & Marketing Directors of International Companies who wish to expand their business reach to Dubai and the Middle East and are looking for a local professional partner to work with.

Requirements
Must have
• Creativity is key. We don't want the normal standard boxes of text and boxes of pics. Be as creative as you like.
Nice to have
• (This is only a suggestion, we welcome your creativity)
- The center of all pages could be large rotating pictures which display professional corporate men/women working in an office, images of Dubai, the UAE, skyscrapers of business towers in Dubai, ..etc.
- Images should reflect Dubai and the Arab World as a modern, fast-paced, growing modern market - Not Traditional)
Should not have
• Not so colorful, the fewer colors you use, the better.
Not Crammed or Busy
Not Traditional but modern

```html
<!DOCTYPE html>
<html lang="en">
<head>
<meta charset="utf-8">
<title>Arcan Group</title>
<link href="https://fonts.googleapis.com/css2?family=Open+Sans:wght@400;600;700&display=swap" rel="stylesheet">
<style>
  :root {
    --page-bg: #2f2f2f;
    --panel: #ffffff;
    --ink: #333333;
    --ink-soft: #444444;
    --accent: #7d1414;
    --rule: #e2e2e2;
    --header-top: #ffffff;
    --header-bottom: #d9d9d9;
    --footer-ink: #f2f2f2;
  }
  * { margin: 0; padding: 0; box-sizing: border-box; }
  html, body {
    width: 1200px; height: 650px; overflow: hidden;
    background: var(--page-bg);
    font-family: "Open Sans", Arial, sans-serif;
    color: var(--ink);
  }
  .site {
    position: absolute; left: 120px; top: 5px;
    width: 960px; height: 616px;
    background: var(--panel);
    border-radius: 4px;
    overflow: hidden;
    box-shadow: 0 1px 4px rgba(0,0,0,.5);
  }
  .site-header {
    position: absolute; left: 0; top: 0; width: 960px; height: 88px;
    background: linear-gradient(to bottom, var(--header-top) 0%, #f1f1f1 45%, var(--header-bottom) 100%);
    border-bottom: 1px solid #b9b9b9;
  }
  .brand {
    position: absolute; left: 40px; top: 31px;
    display: flex; align-items: center; gap: 7px;
    font-size: 17px; font-weight: 600; letter-spacing: .5px; color: var(--ink);
    white-space: nowrap;
  }
  .brand-mark { width: 10px; height: 10px; background: var(--accent); }
  .main-nav {
    position: absolute; right: 25px; top: 33px;
    display: flex; gap: 23px;
    list-style: none;
    font-size: 14.6px; font-weight: 600; color: var(--ink);
    white-space: nowrap;
  }
  .hero {
    position: absolute; left: 0; top: 88px; width: 960px; height: 242px;
    background:
      linear-gradient(to bottom, transparent 55%, rgba(20,12,6,.9) 100%),
      linear-gradient(100deg, #2a2a32 0%, #5a4a3c 25%, #d07a2a 45%, #f0b048 58%, #6f8ea8 78%, #2f5476 100%);
  }
  .hero-copy {
    position: absolute; right: 25px; top: 20px; width: 470px;
    text-align: right; color: #fff;
    text-shadow: 0 1px 2px rgba(0,0,0,.6);
  }
  .hero-title { font-size: 23px; font-weight: 700; letter-spacing: .3px; text-transform: uppercase; line-height: 30px; }
  .hero-quote { font-size: 12.5px; font-weight: 600; line-height: 20px; margin-top: 11px; }
  .hero-more { display: block; font-size: 12.5px; font-weight: 700; line-height: 20px; color: #fff; text-decoration: none; }
  .section-title { font-size: 14px; font-weight: 700; color: var(--accent); }
  .about {
    position: absolute; left: 26px; top: 342px; width: 578px;
  }
  .about-text {
    margin-top: 9px; font-size: 12px; line-height: 18px; color: var(--ink);
    height: 72px; overflow: hidden;
  }
  .read-more { display: block; margin-top: 10px; font-size: 12px; color: var(--accent); text-decoration: none; }
  .divider-v { position: absolute; left: 624px; top: 348px; width: 1px; height: 134px; background: var(--rule); }
  .services { position: absolute; left: 639px; top: 342px; }
  .service-list { margin-top: 10px; list-style: none; font-size: 12px; font-weight: 600; line-height: 18px; color: var(--ink-soft); }
  .service-list li { padding-left: 17px; position: relative; }
  .service-list li::before {
    content: ""; position: absolute; left: 3px; top: 7px;
    width: 5px; height: 5px; border-radius: 50%; background: var(--ink-soft);
  }
  .divider-h { position: absolute; left: 26px; top: 482px; width: 908px; height: 1px; background: var(--rule); }
  .companies { position: absolute; left: 25px; top: 494px; }
  .carousel { position: absolute; left: 55px; top: 536px; width: 852px; height: 52px; }
  .carousel-arrow { position: absolute; top: 14px; }
  .carousel-arrow.prev { left: 10px; }
  .carousel-arrow.next { right: 10px; }
  .carousel-edge { position: absolute; top: 2px; width: 8px; height: 48px; }
  .carousel-edge.left { left: 47px; background: linear-gradient(to right, rgba(0,0,0,.12), transparent); }
  .carousel-edge.right { right: 47px; background: linear-gradient(to left, rgba(0,0,0,.12), transparent); }
  .company-list { position: absolute; left: 60px; top: 0; width: 732px; height: 52px; display: flex; list-style: none; }
  .company {
    flex: 1; display: flex; align-items: center; justify-content: center;
    font-size: 13px; font-weight: 600; letter-spacing: .5px; color: var(--ink);
    white-space: nowrap;
  }
  .site-footer {
    position: absolute; left: 0; top: 628px; width: 1200px;
    text-align: center; font-size: 9.5px; font-weight: 700; color: var(--footer-ink);
  }
</style>
</head>
<body>
  <div class="site">
    <header class="site-header">
      <div class="brand"><span class="brand-mark"></span>ARCAN GROUP</div>
      <ul class="main-nav">
        <li>Home</li>
        <li>About Us</li>
        <li>Chairman’s Message</li>
        <li>Divisions</li>
        <li>Group Companies</li>
        <li>Employment</li>
        <li>Contact us</li>
      </ul>
    </header>

    <section class="hero" role="img" aria-label="Panoramic photo of a city skyline with domes and minarets at sunset under a glowing orange and blue sky">
      <div class="hero-copy">
        <h1 class="hero-title">Welcome to Arcan Group.</h1>
        <p class="hero-quote">“Lorem ipsum dolor sit amet, consectetur adipisicing elit, sed do eiusmod tempor incididunt ut labore et dolore magna aliqua.”</p>
        <a class="hero-more" href="#">Read More</a>
      </div>
    </section>

    <section class="about">
      <h2 class="section-title">About ARCAN GROUP</h2>
      <p class="about-text">ARCAN group is a Dubai-based diversified groups of companies led by its chairman Sheikh Hamad bin Rashid Al Faris, a member of a leading family of Dubai.<br>The Group has grown with Dubai, and while best known for Real Estate Investment, it is globally recog­nized through its involvement in the Legal Consultations, Media Production, General Trading, and Business Services sectors across the region.</p>
      <a class="read-more" href="#">Read more &gt;</a>
    </section>

    <div class="divider-v"></div>

    <section class="services">
      <h2 class="section-title">Our Services</h2>
      <ul class="service-list">
        <li>Legal Services</li>
        <li>Media Production</li>
        <li>Real Estate Investment &amp; Management</li>
        <li>General Trading</li>
        <li>Business Services</li>
        <li>Telecommunication Products &amp; Services</li>
      </ul>
    </section>

    <div class="divider-h"></div>

    <h2 class="section-title companies">Group Companies :</h2>

    <div class="carousel">
      <svg class="carousel-arrow prev" width="22" height="22" viewBox="0 0 22 22"><polyline points="20,4 2,11 20,18" fill="none" stroke="#9a2a2a" stroke-width="1.2"/></svg>
      <div class="carousel-edge left"></div>
      <ul class="company-list">
        <li class="company">ARCAN REAL ESTATE</li>
        <li class="company">ARCAN REAL ESTATE</li>
        <li class="company">ARCAN REAL ESTATE</li>
        <li class="company">ARCAN REAL ESTATE</li>
      </ul>
      <div class="carousel-edge right"></div>
      <svg class="carousel-arrow next" width="22" height="22" viewBox="0 0 22 22"><polyline points="2,4 20,11 2,18" fill="none" stroke="#9a2a2a" stroke-width="1.2"/></svg>
    </div>
  </div>

  <footer class="site-footer">All Rights reserved to Arcan Group 2012</footer>
</body>
</html>
```